inspirational business card

I want to use the Vector on Pixavend.com (number 58172046) and I will purchase the vector to send it to the designer once the general concept is approved. You can download it for free for a one time use on providing a design for this request.
Within the vector, insert:
Tessa Brundle
Guidance and Partnering

I prefer a vertical card but do not require vertical.

Contact info:

Tessa Brundle, J.D.
Collaborative Lawyer
Certified Divorce Coach
Mediation Coach
PHONE 515/555-0143
EMAIL: tbjd@quellmail.net

Website: Guidanceandpartnering.com
Settlementcourse.com

I like greens, blue and grey. I do not want black font, and would like the font to be legible without needing perfect reading vision (no super small font).
I would like the overall theme to convey growth and nurturance.
I like the vector I selected because of the growth and light portrayed.
Not too frilly or too bold. I would like to to appeal to both sexes.

Target Market(s)

Generally professional women 35-60

Industry/Entity Type

Attorney

Font styles to use
Serif
Sans Serif

Colors
acd136
cadf82
fbf289
9d9d9d

Requirements
Must have
• My project does not need to have my photo but you could use it if you want
Nice to have
• Vertical
• I like rounded edges on the cards
Should not have
• I do not like my name appearing two times in close proximity. I'm not a flowery person.

```html
<!DOCTYPE html>
<html lang="en">
<head>
<meta charset="utf-8">
<title>Tessa Brundle, J.D. — Business Card</title>
<link href="https://fonts.googleapis.com/css2?family=Cinzel:wght@400;500&display=swap" rel="stylesheet">
<style>
  :root {
    --lime-top: #9bea0a;
    --lime-bottom: #62bf1c;
    --card-white: #ffffff;
    --emblem-light: #b6e86a;
    --emblem-mid: #7fcf2a;
    --emblem-deep: #4fae1e;
    --rule-green: #9ee21a;
    --ink-grey: #5b6268;
  }
  html, body {
    margin: 0;
    padding: 0;
    overflow: hidden;
    background: #eef2ea;
  }
  .card {
    position: relative;
    width: 686px;
    height: 1200px;
    overflow: hidden;
    background: linear-gradient(180deg, var(--lime-top) 0%, #86d80e 45%, var(--lime-bottom) 100%);
  }
  .card__backdrop {
    position: absolute;
    inset: 0;
  }
  .card__identity {
    position: absolute;
    left: 0;
    right: 0;
    top: 736px;
    text-align: center;
    color: var(--ink-grey);
    font-family: "Cinzel", "Times New Roman", serif;
  }
  .card__name {
    margin: 0;
    font-size: 52px;
    font-weight: 500;
    letter-spacing: 1px;
    line-height: 1;
  }
  .card__rule {
    width: 560px;
    height: 3px;
    margin: 14px auto 0;
    background: var(--rule-green);
  }
  .card__tagline {
    margin: 16px 0 0;
    font-size: 27px;
    font-weight: 400;
    letter-spacing: 1px;
    line-height: 1;
    text-transform: uppercase;
  }
</style>
</head>
<body>
  <div class="card">
    <svg class="card__backdrop" width="686" height="1200" viewBox="0 0 686 1200">
      <defs>
        <filter id="disc-shadow" x="-20%" y="-20%" width="140%" height="140%">
          <feGaussianBlur in="SourceAlpha" stdDeviation="8"/>
          <feOffset dy="3"/>
          <feComponentTransfer><feFuncA type="linear" slope="0.35"/></feComponentTransfer>
          <feMerge><feMergeNode/><feMergeNode in="SourceGraphic"/></feMerge>
        </filter>
        <radialGradient id="emblem-fill" cx="50%" cy="40%" r="60%">
          <stop offset="0%" stop-color="var(--emblem-light)"/>
          <stop offset="65%" stop-color="var(--emblem-mid)"/>
          <stop offset="100%" stop-color="var(--emblem-deep)"/>
        </radialGradient>
      </defs>
      <circle class="card__disc" cx="343" cy="549" r="423" fill="var(--card-white)" filter="url(#disc-shadow)"/>
      <circle class="card__emblem" cx="343" cy="434" r="246" fill="url(#emblem-fill)"
              role="img" aria-label="Tree of life illustration: a leafy green tree with spreading roots inside a crescent ring"/>
    </svg>

    <div class="card__identity">
      <h1 class="card__name">Tessa Brundle, J.D.</h1>
      <div class="card__rule"></div>
      <p class="card__tagline">Guidance &amp; Partnering</p>
    </div>
  </div>
</body>
</html>
```